50th Anniversary Gala Save the date Postcard 8.5x5.5 inches

Looking for a 5.5x8.5 in one-sided postcard design for our annual gala. Design needs to include "Save the date" prominently with all the event information included below. Design should be light, include the colors of our logo and elegant. (almost like a wedding save the date). "Threads of Grace" should look like its own logo.

50th Anniversary Gala at The Lodge at Fernwick Glen – “Threads of Grace – Celebrating 50 Years of Building Community”
Thursday, October 24
6-11p
The Lodge at Fernwick Glen
Marlowe Parkway, New Hyde Park, NY
Honoring – TBW Previous Presidents

Target Market(s)

Exisiting donors

Industry/Entity Type

nonprofit

Font styles to use
Serif
Script

Requirements
Must have
• Save the date prominent
Should not have
• should not have a dark background

```html
<!DOCTYPE html>
<html lang="en">
<head>
<meta charset="utf-8">
<title>Threads of Grace – Save the Date Postcard</title>
<link rel="stylesheet" href="https://fonts.googleapis.com/css2?family=Playfair+Display:ital,wght@0,700;0,800;1,600;1,700&family=Source+Serif+4:ital,wght@0,400;0,600;0,700;1,400;1,600&display=swap">
<style>
  :root {
    --navy: #1d4486;
    --navy-deep: #173a78;
    --sky: #1596d6;
    --sky-light: #4cb0e6;
    --gold: #d4aa3c;
    --gold-light: #f3dc92;
    --green: #6aae45;
    --white: #ffffff;
    --ink: #1b1b1b;
    --stamp: #b3b3b3;
    --page: #e4e4e4;
  }
  * { box-sizing: border-box; margin: 0; padding: 0; }
  html, body { width: 1200px; height: 1117px; overflow: hidden; }
  body { background: var(--page); position: relative; font-family: "Source Serif 4", Georgia, serif; }

  .postcard { position: absolute; left: 228px; width: 745px; height: 482px; background: var(--white); overflow: hidden; }
  .postcard--front { top: 65px; }
  .postcard--back { top: 570px; }
  .postcard svg.art { position: absolute; inset: 0; width: 745px; height: 482px; z-index: 0; }
  .postcard > div, .postcard > p, .postcard > h1, .postcard > h2 { position: absolute; z-index: 1; }

  .org-name { display: flex; align-items: center; gap: 10px; color: var(--navy); font-family: "Source Serif 4", Georgia, serif; font-weight: 700; line-height: 1.05; }
  .org-name .mark { width: 22px; height: 22px; border-radius: 50%; background: var(--gold); flex: none; }
  .postcard--front .org-name { left: 480px; top: 62px; width: 230px; font-size: 27px; }
  .postcard--back .org-name { left: 382px; top: 50px; width: 210px; font-size: 24px; }

  .event-title { left: 425px; top: 182px; width: 300px; text-align: center; font-family: "Playfair Display", Georgia, serif; font-weight: 800; }
  .event-title .line1 { display: block; font-size: 37px; color: var(--navy); letter-spacing: 0.5px; line-height: 1.1; }
  .event-title .line2 { display: block; font-size: 56px; color: var(--sky); line-height: 1; }
  .tagline { left: 420px; top: 297px; width: 310px; text-align: center; font-family: "Source Serif 4", Georgia, serif; font-style: italic; font-size: 28px; line-height: 1.07; color: var(--ink); }
  .tagline strong { color: var(--navy); font-weight: 700; }

  .save-date { font-family: "Playfair Display", Georgia, serif; font-style: italic; font-weight: 700; white-space: nowrap; }
  .postcard--front .save-date { left: 50px; top: 354px; font-size: 33px; color: var(--gold); }
  .postcard--back .save-date { left: 50px; top: 150px; font-size: 37px; color: var(--sky); }

  .date-row { font-family: "Playfair Display", Georgia, serif; font-weight: 700; }
  .date-row .rule { position: absolute; height: 2px; }
  .date-row .day, .date-row .month { position: absolute; font-family: "Source Serif 4", Georgia, serif; font-weight: 700; white-space: nowrap; }
  .date-row .num { position: absolute; text-align: center; font-weight: 800; line-height: 1; }
  .date-row .time { position: absolute; text-align: center; font-weight: 700; line-height: 1; white-space: nowrap; }

  .postcard--front .date-row { left: 0; top: 0; width: 745px; height: 482px; color: var(--white); }
  .postcard--front .rule { background: var(--white); }
  .postcard--front .day { left: 60px; top: 411px; font-size: 24px; }
  .postcard--front .month { left: 270px; top: 411px; font-size: 24px; }
  .postcard--front .num { left: 176px; top: 383px; width: 80px; font-size: 56px; color: var(--sky-light); }
  .postcard--front .time { left: 176px; top: 443px; width: 80px; font-size: 20px; color: var(--sky-light); }

  .postcard--back .date-row { left: 0; top: 0; width: 400px; height: 300px; color: var(--navy); }
  .postcard--back .rule { background: var(--gold); }
  .postcard--back .day { left: 45px; top: 213px; font-size: 22px; }
  .postcard--back .month { left: 236px; top: 213px; font-size: 22px; }
  .postcard--back .num { left: 150px; top: 184px; width: 72px; font-size: 52px; }
  .postcard--back .time { left: 150px; top: 239px; width: 72px; font-size: 19px; }

  .gala-heading { left: 50px; top: 26px; width: 270px; font-family: "Source Serif 4", Georgia, serif; font-weight: 700; font-size: 24px; line-height: 1.2; color: var(--white); }
  .gala-heading .gold { color: var(--gold); font-family: "Playfair Display", Georgia, serif; font-size: 25px; }

  .venue-list { left: 38px; top: 328px; width: 340px; color: var(--white); }
  .venue-item { display: flex; align-items: flex-start; gap: 14px; margin-bottom: 12px; font-weight: 700; font-size: 19px; line-height: 1.12; }
  .venue-item svg { flex: none; width: 28px; height: 30px; }
  .honoring { left: 50px; top: 429px; color: var(--white); font-size: 14px; }
  .honoring strong { font-weight: 700; }

  .stamp-box { left: 630px; top: 31px; width: 82px; height: 82px; background: var(--stamp); }
</style>
</head>
<body>

<section class="postcard postcard--front" aria-label="Postcard front">
  <svg class="art" viewBox="0 0 745 482">
    <defs>
      <linearGradient id="photoTone" x1="0" y1="0" x2="1" y2="1">
        <stop offset="0" stop-color="#2a2420"/>
        <stop offset="0.45" stop-color="#b88a64"/>
        <stop offset="0.75" stop-color="#e7cfae"/>
        <stop offset="1" stop-color="#8f7a70"/>
      </linearGradient>
      <linearGradient id="goldSheen" x1="0" y1="0" x2="1" y2="0">
        <stop offset="0" stop-color="#d4aa3c"/>
        <stop offset="0.3" stop-color="#f3dc92"/>
        <stop offset="0.6" stop-color="#c99a2e"/>
        <stop offset="0.85" stop-color="#f3dc92"/>
        <stop offset="1" stop-color="#d4aa3c"/>
      </linearGradient>
      <linearGradient id="nightBlue" x1="0" y1="0" x2="1" y2="1">
        <stop offset="0" stop-color="#1d4486"/>
        <stop offset="0.7" stop-color="#173a78"/>
        <stop offset="1" stop-color="#1e78c8"/>
      </linearGradient>
    </defs>
    <path role="img" aria-label="Photo: hands raising glasses of sparkling wine in a toast" d="M0 0 H405 C440 80 440 230 350 330 C250 275 120 240 0 265 Z" fill="url(#photoTone)"/>
    <path d="M0 345 C120 290 240 320 360 380 C450 425 540 470 620 470 C690 470 730 440 745 410 V482 H0 Z" fill="url(#nightBlue)"/>
    <path d="M0 345 C120 290 240 320 360 380 C450 425 540 470 620 470" fill="none" stroke="#fff" stroke-width="5"/>
    <path d="M0 255 C100 215 200 250 330 320 C450 390 540 440 610 440 C680 440 730 390 745 335 L745 400 C730 440 690 462 620 462 C540 462 450 420 360 372 C240 310 120 285 0 338 Z" fill="url(#goldSheen)"/>
  </svg>

  <div class="org-name"><span class="mark"></span><span>The Bridgeway Network</span></div>

  <h1 class="event-title"><span class="line1">THREADS OF</span><span class="line2">GRACE</span></h1>
  <p class="tagline">Celebrating <strong>50 Years</strong><br>of Building<br>Community</p>

  <p class="save-date">Save the date</p>
  <div class="date-row">
    <span class="rule" style="left:50px;top:405px;width:127px"></span>
    <span class="rule" style="left:50px;top:446px;width:127px"></span>
    <span class="rule" style="left:254px;top:405px;width:125px"></span>
    <span class="rule" style="left:254px;top:446px;width:125px"></span>
    <span class="day">Thursday</span>
    <span class="num">24</span>
    <span class="time">6–11p</span>
    <span class="month">October</span>
  </div>
</section>

<section class="postcard postcard--back" aria-label="Postcard back">
  <svg class="art" viewBox="0 0 745 482">
    <defs>
      <linearGradient id="goldSweep" x1="0" y1="0" x2="0" y2="1">
        <stop offset="0" stop-color="#d4aa3c"/>
        <stop offset="0.4" stop-color="#f3dc92"/>
        <stop offset="0.7" stop-color="#c99a2e"/>
        <stop offset="1" stop-color="#e9c96a"/>
      </linearGradient>
      <linearGradient id="topBlue" x1="0" y1="0" x2="1" y2="1">
        <stop offset="0" stop-color="#1e63b0"/>
        <stop offset="1" stop-color="#173a78"/>
      </linearGradient>
      <linearGradient id="panelBlue" x1="0" y1="0" x2="1" y2="1">
        <stop offset="0" stop-color="#1596d6"/>
        <stop offset="1" stop-color="#1a7cc4"/>
      </linearGradient>
      <linearGradient id="greenBar" x1="0" y1="0" x2="1" y2="0">
        <stop offset="0" stop-color="#6aae45"/>
        <stop offset="0.45" stop-color="#cde59b"/>
        <stop offset="1" stop-color="#6aae45"/>
      </linearGradient>
    </defs>
    <path d="M0 0 H335 C312 50 312 100 322 132 H0 Z" fill="url(#topBlue)"/>
    <rect x="0" y="274" width="380" height="13" fill="url(#greenBar)"/>
    <path d="M0 302 H392 C410 370 405 430 375 482 H0 Z" fill="url(#panelBlue)"/>
    <path d="M319 0 C300 60 330 150 370 260 C410 360 420 430 370 482 H442 C475 400 432 300 402 220 C372 140 350 60 388 0 Z" fill="url(#goldSweep)"/>
    <path d="M344 0 C322 60 350 150 390 260 C428 360 432 430 395 482" fill="none" stroke="#fff" stroke-width="4"/>
  </svg>

  <h2 class="gala-heading"><span class="gold">50th Anniversary</span><br>Gala at The Lodge at<br>Fernwick Glen</h2>

  <p class="save-date">Save the date</p>
  <div class="date-row">
    <span class="rule" style="left:37px;top:208px;width:115px"></span>
    <span class="rule" style="left:37px;top:244px;width:115px"></span>
    <span class="rule" style="left:220px;top:208px;width:114px"></span>
    <span class="rule" style="left:220px;top:244px;width:114px"></span>
    <span class="day">Thursday</span>
    <span class="num">24</span>
    <span class="time">6–11p</span>
    <span class="month">October</span>
  </div>

  <div class="venue-list">
    <p class="venue-item">
      <svg viewBox="0 0 28 30" fill="none" stroke="#fff" stroke-width="1.4"><path d="M4 29 V10 L14 3 L24 10 V29 Z"/><path d="M1 29 H27"/><rect x="8" y="12" width="3" height="3"/><rect x="12.5" y="12" width="3" height="3"/><rect x="17" y="12" width="3" height="3"/><rect x="8" y="18" width="3" height="3"/><rect x="17" y="18" width="3" height="3"/><path d="M12 29 V22 H16 V29"/></svg>
      <span>The Lodge at Fernwick Glen</span>
    </p>
    <p class="venue-item">
      <svg viewBox="0 0 28 30" fill="none" stroke="#fff" stroke-width="1.5"><path d="M14 25 C8 17 6 14 6 10 A8 8 0 0 1 22 10 C22 14 20 17 14 25 Z"/><circle cx="14" cy="10" r="3"/><ellipse cx="14" cy="26" rx="8" ry="2.5"/></svg>
      <span>Marlowe Parkway, New<br>Hyde Park, NY</span>
    </p>
  </div>
  <p class="honoring"><strong>Honoring –</strong> TBW Previous Presidents</p>

  <div class="org-name"><span class="mark"></span><span>The Bridgeway Network</span></div>
  <div class="stamp-box" aria-label="Postage area"></div>
</section>

</body>
</html>
```